Elegant, professional powerpoint design for Varomel Engineering and Mining SARLU

I’ve created a new Sub contracting company for mining industry in the Democratic Republic of Congo. With Quorvixel, I’ve created a logo. I would want a professional and beautiful powerpoint design which I will use to sell my services to mining companies in DRC. The powerpoint must have pictures of mining engines such as excavators, drones, trucks, etc

```html
<!DOCTYPE html>
<html lang="en">
<head>
<meta charset="utf-8">
<title>Varomel Engineering and Mining SARLU – Presentation Deck</title>
<link rel="stylesheet" href="https://fonts.googleapis.com/css2?family=Open+Sans:wght@400;600;700;800&display=swap">
<style>
:root{
  --gold:#e0a100;
  --gold-dark:#b97f00;
  --ink:#1f1f1f;
  --grey:#8a8a8a;
  --line:#dcdcdc;
  --page:#f3f3f3;
  --navy:#1b2a8c;
  --navy-deep:#14207a;
  --dark:#1a1a1a;
  --icon:#3a3a3a;
}
*{box-sizing:border-box;margin:0;padding:0}
html,body{width:1200px;height:753px;overflow:hidden;background:var(--page);font-family:"Open Sans",sans-serif;color:var(--ink)}
.deck{position:relative;width:1200px;height:753px}
.defs{position:absolute;width:0;height:0;overflow:hidden}
.slide{position:absolute;width:171px;height:95px;background:#fff;overflow:hidden;box-shadow:0 2px 6px rgba(0,0,0,.09)}
.c1{left:42px}.c2{left:231px}.c3{left:420px}.c4{left:609px}.c5{left:797px}.c6{left:987px}
.r1{top:42px}.r2{top:157px}.r3{top:272px}.r4{top:387px}.r5{top:501px}.r6{top:616px}
.dark{background:var(--dark);color:#fff}
.navy{background:linear-gradient(135deg,var(--navy-deep),var(--navy));color:#fff}
.abs{position:absolute}
.title{position:absolute;top:9px;left:0;width:100%;text-align:center;font-weight:700;font-size:6.2px;color:var(--ink)}
.title::before{content:"";display:block;width:7px;height:.8px;background:var(--gold);margin:0 auto 1.5px}
.title b{color:var(--gold);font-weight:700}
.navy .title,.navy .title b{color:#fff}
.sub{font-size:2px;font-weight:400;color:var(--grey);text-align:center}
.tx{font-size:2.1px;line-height:2.8px;color:#666}
.tx.w{color:#eee}
.h{font-size:2.5px;font-weight:700;color:var(--ink)}
.foot{position:absolute;left:0;right:0;bottom:4px;height:3px;background:linear-gradient(90deg,var(--gold-dark),var(--gold));font-size:1.8px;color:#fff;text-align:center;line-height:3px}
.foot .pg{position:absolute;right:4px;top:0}
.badge{position:absolute;left:3px;bottom:2.5px;width:6px;height:6px;background:#fff;border:.6px solid var(--gold);border-radius:1px}
.brand{font-weight:800;color:var(--gold);letter-spacing:.2px}
.photo{position:absolute;border-radius:1px}
.p-earth{background:linear-gradient(160deg,#c9a37c,#8e6a4a 60%,#5b4634)}
.p-truck{background:linear-gradient(180deg,#9fb4c8 0%,#b8b1a2 45%,#6d5f4c 100%)}
.p-pit{background:linear-gradient(135deg,#d7c3a8,#a88e72 50%,#7a6957)}
.p-dig{background:linear-gradient(180deg,#cfd9e0,#b59a72 55%,#6f5a40)}
.p-dark{background:radial-gradient(circle at 30% 40%,#4b443a,#1b1a18 70%)}
.cover-name{font-size:2.8px;font-weight:700}
.cover-name span{color:var(--gold)}
.gold-box{background:linear-gradient(135deg,#e6a800,#b77a00);color:#fff}
.avatar{border-radius:50%;background:linear-gradient(160deg,#c9cfd6,#8f98a3)}
.icon-sheet{position:absolute;left:7px;top:7px}
</style>
</head>
<body>
<svg class="defs" aria-hidden="true">
  <defs>
    <symbol id="i-phone" viewBox="0 0 24 24"><path d="M5 3h4l2 5-3 2a11 11 0 0 0 6 6l2-3 5 2v4a2 2 0 0 1-2 2A17 17 0 0 1 3 5a2 2 0 0 1 2-2z"/></symbol>
    <symbol id="i-pin" viewBox="0 0 24 24"><path d="M12 22s7-7 7-12a7 7 0 0 0-14 0c0 5 7 12 7 12z"/><circle cx="12" cy="10" r="2.5"/></symbol>
    <symbol id="i-tick" viewBox="0 0 24 24"><circle cx="12" cy="12" r="9"/><path d="M8 12l3 3 5-6"/></symbol>
    <symbol id="i-mail" viewBox="0 0 24 24"><rect x="3" y="6" width="18" height="12" rx="1"/><path d="M3 7l9 6 9-6"/></symbol>
    <symbol id="i-search" viewBox="0 0 24 24"><circle cx="10" cy="10" r="6"/><path d="M15 15l6 6"/></symbol>
    <symbol id="i-user" viewBox="0 0 24 24"><circle cx="12" cy="8" r="4"/><path d="M4 21a8 8 0 0 1 16 0"/></symbol>
    <symbol id="i-home" viewBox="0 0 24 24"><path d="M3 11l9-8 9 8M5 10v10h14V10"/></symbol>
    <symbol id="i-chart" viewBox="0 0 24 24"><path d="M4 20h16M7 17v-5M12 17V7M17 17v-8"/></symbol>
    <symbol id="i-clock" viewBox="0 0 24 24"><circle cx="12" cy="12" r="9"/><path d="M12 7v5l3 2"/></symbol>
    <symbol id="i-star" viewBox="0 0 24 24"><path d="M12 3l2.6 6 6.4.5-5 4.2 1.6 6.3L12 16.6 6.4 20l1.6-6.3-5-4.2 6.4-.5z"/></symbol>
    <symbol id="i-lock" viewBox="0 0 24 24"><rect x="5" y="11" width="14" height="10" rx="1"/><path d="M8 11V7a4 4 0 0 1 8 0v4"/></symbol>
    <symbol id="i-doc" viewBox="0 0 24 24"><path d="M6 3h8l4 4v14H6zM14 3v4h4M9 12h6M9 16h6"/></symbol>
    <symbol id="i-cloud" viewBox="0 0 24 24"><path d="M7 18h10a4 4 0 0 0 0-8 6 6 0 0 0-11 1 3.5 3.5 0 0 0 1 7z"/></symbol>
    <symbol id="i-bell" viewBox="0 0 24 24"><path d="M6 16v-5a6 6 0 0 1 12 0v5l2 2H4zM10 21h4"/></symbol>
    <symbol id="i-gear" viewBox="0 0 24 24"><circle cx="12" cy="12" r="4"/><path d="M12 2v4M12 18v4M2 12h4M18 12h4M5 5l3 3M16 16l3 3M5 19l3-3M16 8l3-3"/></symbol>
    <symbol id="i-arrow" viewBox="0 0 24 24"><path d="M4 12h15M13 6l6 6-6 6"/></symbol>
    <symbol id="i-flag" viewBox="0 0 24 24"><path d="M5 21V4h12l-3 4 3 4H5"/></symbol>
    <symbol id="i-case" viewBox="0 0 24 24"><rect x="3" y="7" width="18" height="13" rx="1"/><path d="M9 7V4h6v3M3 12h18"/></symbol>
    <symbol id="i-pie" viewBox="0 0 24 24"><path d="M11 4v9h9a9 9 0 1 1-9-9zM14 2a8 8 0 0 1 8 8h-8z"/></symbol>
    <symbol id="i-team" viewBox="0 0 24 24"><circle cx="8" cy="8" r="3"/><circle cx="16" cy="8" r="3"/><path d="M2 20a6 6 0 0 1 12 0M10 20a6 6 0 0 1 12 0"/></symbol>
    <symbol id="i-rocket" viewBox="0 0 24 24"><path d="M12 2c4 3 5 8 3 14H9C7 10 8 5 12 2zM9 16l-3 4h4M15 16l3 4h-4"/><circle cx="12" cy="9" r="1.8"/></symbol>
    <symbol id="i-monitor" viewBox="0 0 24 24"><rect x="3" y="4" width="18" height="12" rx="1"/><path d="M9 20h6M12 16v4"/></symbol>

    <pattern id="icons-a" patternUnits="userSpaceOnUse" width="78.4" height="40.5">
      <g fill="none" stroke="#3a3a3a" stroke-width="2" stroke-linecap="round" stroke-linejoin="round">
        <use href="#i-phone" x="2.4" y="4" width="5" height="5"/><use href="#i-pin" x="12.2" y="4" width="5" height="5"/><use href="#i-tick" x="22" y="4" width="5" height="5"/><use href="#i-mail" x="31.8" y="4" width="5" height="5"/><use href="#i-search" x="41.6" y="4" width="5" height="5"/><use href="#i-user" x="51.4" y="4" width="5" height="5"/><use href="#i-home" x="61.2" y="4" width="5" height="5"/><use href="#i-chart" x="71" y="4" width="5" height="5"/>
        <use href="#i-clock" x="2.4" y="17.5" width="5" height="5"/><use href="#i-star" x="12.2" y="17.5" width="5" height="5"/><use href="#i-lock" x="22" y="17.5" width="5" height="5"/><use href="#i-doc" x="31.8" y="17.5" width="5" height="5"/><use href="#i-cloud" x="41.6" y="17.5" width="5" height="5"/><use href="#i-bell" x="51.4" y="17.5" width="5" height="5"/><use href="#i-gear" x="61.2" y="17.5" width="5" height="5"/><use href="#i-arrow" x="71" y="17.5" width="5" height="5"/>
        <use href="#i-flag" x="2.4" y="31" width="5" height="5"/><use href="#i-case" x="12.2" y="31" width="5" height="5"/><use href="#i-pie" x="22" y="31" width="5" height="5"/><use href="#i-team" x="31.8" y="31" width="5" height="5"/><use href="#i-rocket" x="41.6" y="31" width="5" height="5"/><use href="#i-monitor" x="51.4" y="31" width="5" height="5"/><use href="#i-phone" x="61.2" y="31" width="5" height="5"/><use href="#i-tick" x="71" y="31" width="5" height="5"/>
      </g>
    </pattern>
    <pattern id="icons-b" patternUnits="userSpaceOnUse" width="78.4" height="40.5">
      <g fill="none" stroke="#3a3a3a" stroke-width="2" stroke-linecap="round" stroke-linejoin="round">
        <use href="#i-case" x="2.4" y="4" width="5" height="5"/><use href="#i-monitor" x="12.2" y="4" width="5" height="5"/><use href="#i-team" x="22" y="4" width="5" height="5"/><use href="#i-gear" x="31.8" y="4" width="5" height="5"/><use href="#i-flag" x="41.6" y="4" width="5" height="5"/><use href="#i-doc" x="51.4" y="4" width="5" height="5"/><use href="#i-rocket" x="61.2" y="4" width="5" height="5"/><use href="#i-lock" x="71" y="4" width="5" height="5"/>
        <use href="#i-pie" x="2.4" y="17.5" width="5" height="5"/><use href="#i-arrow" x="12.2" y="17.5" width="5" height="5"/><use href="#i-home" x="22" y="17.5" width="5" height="5"/><use href="#i-bell" x="31.8" y="17.5" width="5" height="5"/><use href="#i-mail" x="41.6" y="17.5" width="5" height="5"/><use href="#i-star" x="51.4" y="17.5" width="5" height="5"/><use href="#i-pin" x="61.2" y="17.5" width="5" height="5"/><use href="#i-cloud" x="71" y="17.5" width="5" height="5"/>
        <use href="#i-chart" x="2.4" y="31" width="5" height="5"/><use href="#i-user" x="12.2" y="31" width="5" height="5"/><use href="#i-clock" x="22" y="31" width="5" height="5"/><use href="#i-search" x="31.8" y="31" width="5" height="5"/><use href="#i-tick" x="41.6" y="31" width="5" height="5"/><use href="#i-phone" x="51.4" y="31" width="5" height="5"/><use href="#i-case" x="61.2" y="31" width="5" height="5"/><use href="#i-gear" x="71" y="31" width="5" height="5"/>
      </g>
    </pattern>
  </defs>
</svg>
<main class="deck">

<!-- ROW 1 -->
<section class="slide dark c1 r1">
  <div class="photo p-dark" style="inset:0" role="img" aria-label="Dark photo of a mining excavator at a quarry"></div>
  <div class="abs" style="top:17px;width:100%;text-align:center">
    <div class="brand" style="font-size:4.5px">VAROMEL</div>
    <div style="font-size:1.5px;color:var(--gold)">ENGINEERING AND MINING</div>
    <div style="font-size:5.2px;font-weight:700;margin-top:7px">Presentation Tittle Goes Here</div>
    <div style="font-size:2.3px;color:#ccc;margin-top:1px">Credential Subtitle Presentation</div>
    <div class="cover-name" style="margin-top:7px">Mr. Daniel <span>Moreau</span></div>
  </div>
  <div class="abs" style="left:8px;bottom:6px;font-size:1.8px;color:#bbb"><span style="color:var(--gold)">January</span> 2023</div>
  <div class="abs" style="right:8px;bottom:6px;font-size:1.8px;color:#bbb">varomel-mining.cd</div>
</section>

<section class="slide dark c2 r1">
  <div class="photo p-dark" style="inset:0;opacity:.8" role="img" aria-label="Dark background photo of mining site"></div>
  <div class="photo p-pit" style="left:100px;top:12px;width:58px;height:70px;clip-path:polygon(50% 0,100% 25%,100% 75%,50% 100%,0 75%,0 25%)" role="img" aria-label="Hexagon framed photo of an open pit mine"></div>
  <div class="abs" style="left:8px;top:39px">
    <div style="font-size:5px;font-weight:700">Presentation Tittle Goes Here</div>
    <div style="font-size:2.3px;color:#ccc;margin-top:1px">Credential Subtitle Presentation</div>
    <div class="cover-name" style="margin-top:7px">Mr. Daniel <span>Moreau</span></div>
  </div>
  <div class="abs" style="left:8px;bottom:6px;font-size:1.8px;color:#bbb"><span style="color:var(--gold)">January</span> 2023</div>
</section>

<section class="slide c3 r1">
  <div class="abs" style="top:17px;width:100%;text-align:center">
    <div class="brand" style="font-size:4.5px">VAROMEL</div>
    <div style="font-size:1.5px;color:var(--gold)">ENGINEERING AND MINING</div>
    <div style="font-size:5.2px;font-weight:700;margin-top:7px">Presentation Tittle Goes Here</div>
    <div style="font-size:2.3px;color:var(--gold);margin-top:1px">Credential Subtitle Presentation</div>
    <div class="cover-name" style="margin-top:7px">Mr. Daniel <span>Moreau</span></div>
  </div>
  <div class="abs" style="left:8px;bottom:6px;font-size:1.8px;color:#999"><span style="color:var(--gold)">January</span> 2023</div>
  <div class="abs" style="right:8px;bottom:6px;font-size:1.8px;color:#999">varomel-mining.cd</div>
</section>

<section class="slide c4 r1">
  <div class="abs" style="left:8px;top:14px">
    <div class="brand" style="font-size:4.5px">VAROMEL</div>
    <div style="font-size:1.5px;color:var(--gold)">ENGINEERING AND MINING</div>
    <div style="font-size:5.2px;font-weight:700;margin-top:6px">Presentation Tittle Goes Here</div>
    <div style="font-size:2.3px;color:var(--grey);margin-top:1px">Credential Subtitle Presentation</div>
    <div class="cover-name" style="margin-top:7px">Mr. Daniel <span>Moreau</span></div>
  </div>
  <div class="abs" style="left:8px;bottom:6px;font-size:1.8px;color:#999"><span style="color:var(--gold)">January</span> 2023</div>
  <div class="abs" style="right:8px;bottom:6px;font-size:1.8px;color:#999">varomel-mining.cd</div>
</section>

<section class="slide c5 r1">
  <div class="title" style="top:7px">Presentation List<div class="sub">Here Our Credential Subtitle</div></div>
  <svg class="abs" style="left:22px;top:30px" width="130" height="48" viewBox="0 0 130 48" font-family="Open Sans, sans-serif" font-size="2" font-weight="700">
    <g fill="#333">
      <text x="0" y="3">COVER SLIDES</text><text x="50" y="3">01</text>
      <text x="0" y="15.5" fill="#e0a100">PRESENTATION LIST</text><text x="50" y="15.5" fill="#e0a100">03</text>
      <text x="0" y="28">ABOUT US</text><text x="50" y="28">04</text>
      <text x="0" y="40.5">OUR MISSIONS &amp; VISION</text><text x="50" y="40.5">06</text>
      <text x="74" y="3">INFOGRAPH ONE</text><text x="124" y="3">07</text>
      <text x="74" y="15.5">INFOGRAPH TWO</text><text x="124" y="15.5">08</text>
      <text x="74" y="28">INFOGRAPH THREE</text><text x="124" y="28">09</text>
      <text x="74" y="40.5">CLOSING SLIDES</text><text x="124" y="40.5">10</text>
    </g>
    <g stroke="#999" stroke-width=".3"><line x1="0" y1="5" x2="52" y2="5"/><line x1="0" y1="17.5" x2="52" y2="17.5" stroke="#e0a100"/><line x1="0" y1="30" x2="52" y2="30"/><line x1="0" y1="42.5" x2="52" y2="42.5"/><line x1="74" y1="5" x2="126" y2="5"/><line x1="74" y1="17.5" x2="126" y2="17.5"/><line x1="74" y1="30" x2="126" y2="30"/><line x1="74" y1="42.5" x2="126" y2="42.5"/></g>
  </svg>
  <div class="foot">varomel-mining.cd<span class="pg">page | 5</span></div><div class="badge"></div>
</section>

<section class="slide c6 r1">
  <div class="title" style="top:7px">Our <b>Vision</b><div class="sub">Here Our Credential Subtitle</div></div>
  <div class="abs gold-box" style="left:21px;top:28px;width:129px;height:44px;font-size:2.9px;line-height:4.4px;text-align:center;padding:10px 8px;font-style:italic">Lorem ipsum dolor sit amet, consectetuer adipiscing elit. Maecenas porttitor congue massa. Fusce posuere, magna sed pulvinar ultricies, purus lectus malesuada libero.</div>
  <div class="foot">varomel-mining.cd<span class="pg">page | 6</span></div><div class="badge"></div>
</section>

<!-- ROW 2 -->
<section class="slide c1 r2">
  <div class="title" style="top:7px">Our <b>Mission</b></div>
  <div class="abs" style="left:16px;top:28px;width:140px;display:grid;grid-template-columns:repeat(3,1fr);column-gap:8px;row-gap:8px;text-align:center">
    <div><div class="h">Mission One</div><div class="tx">Our crews deliver safe, reliable haulage on every site.</div></div>
    <div class="gold-box" style="padding:2px"><div class="h" style="color:#fff">Mission Two</div><div class="tx w">We plan and build mine roads, pads and benches on time.</div></div>
    <div><div class="h">Mission Three</div><div class="tx">Modern fleets keep output steady all year round.</div></div>
    <div><div class="h">Mission Four</div><div class="tx">We train local teams and grow skills across the region.</div></div>
    <div><div class="h">Mission Five</div><div class="tx">Clear reporting gives clients full control of costs.</div></div>
    <div><div class="h">Mission Six</div><div class="tx">We protect land, water and the communities we serve.</div></div>
  </div>
  <div class="foot">varomel-mining.cd<span class="pg">page | 7</span></div><div class="badge"></div>
</section>

<section class="slide c2 r2">
  <div class="photo p-dig" style="left:18px;top:24px;width:46px;height:41px" role="img" aria-label="Photo of an orange excavator digging"></div>
  <div class="abs" style="left:77px;top:24px;width:80px">
    <div style="font-size:5.8px;font-weight:700">Our <span style="color:var(--gold)">Legacy</span></div>
    <div style="width:7px;height:.8px;background:var(--gold);margin:1px 0 2px"></div>
    <div class="tx">Founded to serve the mining belt with equipment, skilled crews and dependable contract work.</div>
    <div style="display:flex;gap:2px;margin-top:5px;text-align:center">
      <div style="width:15px"><div style="font-size:3.6px;font-weight:700">12+</div><div class="tx">Partnership</div></div>
      <div class="gold-box" style="width:15px"><div style="font-size:3.6px;font-weight:700">400+</div><div class="tx w">Satisfy Cost</div></div>
      <div style="width:15px"><div style="font-size:3.6px;font-weight:700">120+</div><div class="tx">Employee</div></div>
    </div>
  </div>
  <div class="foot">varomel-mining.cd<span class="pg">page | 8</span></div><div class="badge"></div>
</section>

<section class="slide c3 r2">
  <div class="title" style="top:7px">Our <b>Pictures</b><div class="sub">Here Our Credential Subtitle</div></div>
  <div class="photo p-truck" style="left:12px;top:25px;width:40px;height:31px" role="img" aria-label="Photo of yellow haul truck on gravel"></div>
  <div class="photo p-earth" style="left:66px;top:25px;width:40px;height:31px" role="img" aria-label="Aerial photo of trucks at an earthworks site"></div>
  <div class="photo" style="left:120px;top:25px;width:40px;height:31px;background:linear-gradient(160deg,#7d8a96,#6a5d4e)" role="img" aria-label="Photo of loading equipment in a pit"></div>
  <div class="abs" style="left:12px;top:58px;width:148px;display:flex;justify-content:space-between;text-align:center">
    <div style="width:40px"><div class="h">Picture One</div><div class="tx">Haul trucks moving ore to the plant.</div></div>
    <div style="width:40px"><div class="h">Picture Two</div><div class="tx">Site survey and earthworks layout.</div></div>
    <div style="width:40px"><div class="h">Picture Three</div><div class="tx">Loading fleet at the open pit face.</div></div>
  </div>
  <div class="foot">varomel-mining.cd<span class="pg">page | 9</span></div><div class="badge"></div>
</section>

<section class="slide c4 r2">
  <div class="title" style="top:10px">Our <b>Company</b><div class="sub">Here Our Credential Subtitle</div></div>
  <div class="abs tx" style="left:22px;top:34px;width:127px;text-align:center">We are a subcontractor for the mining industry, offering excavation, haulage, drilling support and drone survey, with safety first and local hiring on every project.</div>
  <div class="abs" style="left:14px;top:60px;width:144px;display:flex;justify-content:space-between;text-align:center">
    <div><div style="font-size:4.2px">1092</div><div class="tx">Project Done</div></div>
    <div><div style="font-size:4.2px">120</div><div class="tx">Satisfy Costumer</div></div>
    <div><div style="font-size:4.2px">45</div><div class="tx">Global Partnership</div></div>
    <div><div style="font-size:4.2px">23+</div><div class="tx">Certifications Company</div></div>
  </div>
  <div class="foot">varomel-mining.cd<span class="pg">page | 10</span></div><div class="badge"></div>
</section>

<section class="slide c5 r2">
  <div class="title" style="top:10px">Analyse <b>Chart</b></div>
  <svg class="abs" style="left:10px;top:28px" width="58" height="50" viewBox="0 0 58 50" font-family="Open Sans, sans-serif" font-size="1.9" fill="#444">
    <text x="2" y="2">Finding Chart</text>
    <text x="2" y="14">Data Five</text><rect x="20" y="12" width="7" height="2" fill="#f0c040"/>
    <text x="2" y="19.5">Data Four</text><rect x="20" y="17.5" width="9" height="2" fill="#8b94a8"/>
    <text x="2" y="25">Data Three</text><rect x="20" y="23" width="18" height="2" fill="#2a3a8c"/>
    <text x="2" y="30.5">Data Two</text><rect x="20" y="28.5" width="20" height="2" fill="#3a4aa0"/>
    <text x="2" y="36">Data One</text><rect x="20" y="34" width="22" height="2" fill="#e0a100"/>
    <text x="20" y="43">0</text><text x="32" y="43">100</text><text x="44" y="43">200</text>
  </svg>
  <div class="abs" style="left:76px;top:28px;width:84px;height:50px;box-shadow:0 0 3px rgba(0,0,0,.12);padding:3px 5px">
    <div class="h" style="font-size:2.1px">Analyse One:</div><div class="tx">Output rose as the new haul fleet came into service.</div>
    <div class="h" style="font-size:2.1px;margin-top:1.5px">Analyse Two:</div><div class="tx">Fuel cost per tonne fell after better route planning.</div>
    <div class="h" style="font-size:2.1px;margin-top:1.5px">Analyse Three:</div><div class="tx">Downtime dropped thanks to planned upkeep.</div>
  </div>
  <div class="foot">varomel-mining.cd<span class="pg">page | 11</span></div><div class="badge"></div>
</section>

<section class="slide c6 r2">
  <div class="title" style="top:14px">S.W.O.T <b>Analyse</b></div>
  <div class="abs tx" style="left:23px;top:30px;width:125px;text-align:center">Our review of strengths, weak points, openings and threats guides every bid we make to mining clients.</div>
  <div class="abs" style="left:12px;top:46px;width:150px;display:flex;gap:2px">
    <div style="flex:1;padding:2px"><div style="font-size:2.8px">Strenght</div><div class="tx">1 Strong fleet plan<br>2 Growth strategy<br>3 Skilled crews<br>4 Fast mobilising</div></div>
    <div class="gold-box" style="flex:1;padding:2px"><div style="font-size:2.8px">Weakness</div><div class="tx w">1 Young brand<br>2 Limited spares<br>3 Small workshop<br>4 Few contracts</div></div>
    <div style="flex:1;padding:2px"><div style="font-size:2.8px">Opportunity</div><div class="tx">1 New copper sites<br>2 Cobalt growth<br>3 Drone survey<br>4 Local content</div></div>
    <div style="flex:1;padding:2px"><div style="font-size:2.8px">Thread</div><div class="tx">1 Price swings<br>2 Road access<br>3 Rain seasons<br>4 New rivals</div></div>
  </div>
  <div class="foot">varomel-mining.cd<span class="pg">page | 12</span></div><div class="badge"></div>
</section>

<!-- ROW 3 -->
<section class="slide c1 r3">
  <div class="photo p-pit" style="left:10px;top:0;width:60px;height:73px" role="img" aria-label="Aerial photo of an open pit mine"></div>
  <div class="abs" style="left:86px;top:13px;width:75px">
    <div style="font-size:5.8px;font-weight:700">Our <span style="color:var(--gold)">Step</span></div>
    <div class="tx" style="margin-top:1px">How we run a new contract from survey to handover.</div>
    <div class="h" style="margin-top:3px;font-size:2.1px">First <span style="color:var(--gold)">Step</span></div><div class="tx">Site visit, drone survey and scope.</div>
    <div class="h" style="margin-top:3px;font-size:2.1px">Second <span style="color:var(--gold)">Step</span></div><div class="tx">Fleet mobilising and crew training.</div>
    <div class="h" style="margin-top:3px;font-size:2.1px">Third <span style="color:var(--gold)">Step</span></div><div class="tx">Daily work, reports and review.</div>
  </div>
  <div class="foot">varomel-mining.cd<span class="pg">page | 13</span></div><div class="badge"></div>
</section>

<section class="slide c2 r3">
  <div class="photo p-truck" style="left:0;top:16px;width:86px;height:61px" role="img" aria-label="Photo of a large mining dump truck in a quarry"></div>
  <div class="abs" style="left:95px;top:16px;width:70px">
    <div style="font-size:5.8px;font-weight:700">Our <span style="color:var(--gold)">Plan</span></div>
    <div class="tx" style="margin-top:1px;color:var(--gold)">Our plan for the next three years of growth.</div>
    <div class="h" style="margin-top:4px;font-size:2.1px;color:var(--gold)">• First Plan</div><div class="tx">Add ten haul trucks<br>Open a new workshop<br>Hire local operators</div>
    <div class="h" style="margin-top:3px;font-size:2.1px;color:var(--gold)">• Second Plan</div><div class="tx">Launch drone survey<br>Win two new sites<br>Pass full safety audit</div>
  </div>
  <div class="foot">varomel-mining.cd<span class="pg">page | 14</span></div><div class="badge"></div>
</section>

<section class="slide c3 r3">
  <div class="photo p-dig" style="left:6px;top:9px;width:35px;height:34px" role="img" aria-label="Photo of excavators at work"></div>
  <div class="photo p-truck" style="left:77px;top:9px;width:35px;height:34px" role="img" aria-label="Photo of a haul truck under blue sky"></div>
  <div class="photo p-earth" style="left:42px;top:45px;width:35px;height:34px" role="img" aria-label="Photo of a dump truck front view"></div>
  <div class="abs tx" style="left:44px;top:18px;width:31px">Excavation for pit benches and ramps.</div>
  <div class="abs tx" style="left:7px;top:54px;width:32px">Site haulage with our own fleet.</div>
  <div class="abs tx" style="left:80px;top:54px;width:31px">Heavy loads moved day and night.</div>
  <div class="abs" style="left:120px;top:34px;width:47px">
    <div style="width:7px;height:.8px;background:var(--gold);margin-bottom:1.5px"></div>
    <div style="font-size:5.8px;font-weight:700">Portfolio</div>
    <div class="tx" style="margin-top:1px">Recent work for large copper and cobalt mines.</div>
  </div>
  <div class="foot">varomel-mining.cd<span class="pg">page | 15</span></div><div class="badge"></div>
</section>

<section class="slide c4 r3">
  <div class="title" style="top:9px">Company <b>Leader</b></div>
  <div class="abs" style="left:13px;top:24px;width:146px;display:flex;gap:2px">
    <div style="flex:1;text-align:center"><div class="gold-box" style="height:17px;position:relative"><div class="avatar abs" style="left:11px;top:3px;width:14px;height:14px" role="img" aria-label="Leader portrait"></div></div><div class="h" style="margin-top:3px;font-size:2.1px">Nadia <span style="color:var(--gold)">Ilunga</span></div><div class="tx">Manager of Lorem</div><div class="tx" style="text-align:left;margin-top:1px">• Leads site planning<br>• Runs client talks<br>• Signs off budgets</div></div>
    <div style="flex:1;text-align:center"><div class="gold-box" style="height:17px;position:relative"><div class="avatar abs" style="left:11px;top:3px;width:14px;height:14px" role="img" aria-label="Leader portrait"></div></div><div class="h" style="margin-top:3px;font-size:2.1px">Grace <span style="color:var(--gold)">Kabila</span></div><div class="tx">Manager of Lorem</div><div class="tx" style="text-align:left;margin-top:1px">• Leads operations<br>• Manages fleets<br>• Tracks output</div></div>
    <div style="flex:1;text-align:center"><div class="gold-box" style="height:17px;position:relative"><div class="avatar abs" style="left:11px;top:3px;width:14px;height:14px" role="img" aria-label="Leader portrait"></div></div><div class="h" style="margin-top:3px;font-size:2.1px">Paul <span style="color:var(--gold)">Mbuyi</span></div><div class="tx">Manager of Lorem</div><div class="tx" style="text-align:left;margin-top:1px">• Leads safety<br>• Trains crews<br>• Audits sites</div></div>
    <div style="flex:1;text-align:center"><div class="gold-box" style="height:17px;position:relative"><div class="avatar abs" style="left:11px;top:3px;width:14px;height:14px" role="img" aria-label="Leader portrait"></div></div><div class="h" style="margin-top:3px;font-size:2.1px">Rita <span style="color:var(--gold)">Kasongo</span></div><div class="tx">Manager of Lorem</div><div class="tx" style="text-align:left;margin-top:1px">• Leads finance<br>• Buys equipment<br>• Reports costs</div></div>
  </div>
  <div class="foot">varomel-mining.cd<span class="pg">page | 16</span></div><div class="badge"></div>
</section>

<section class="slide c5 r3">
  <div class="title" style="top:9px"><b>Member</b> Team</div>
  <div class="abs gold-box" style="left:14px;top:23px;width:70px;height:14px;border-radius:1px">
    <div class="avatar abs" style="left:4px;top:2px;width:10px;height:10px" role="img" aria-label="Team member portrait"></div>
    <div class="abs" style="left:29px;top:3.5px;font-size:2.8px;font-weight:700">Esther Banza</div>
    <div class="abs" style="left:29px;top:8px;font-size:1.9px">Marketing Manager</div>
  </div>
  <div class="abs" style="left:92px;top:23px;width:70px;display:flex;justify-content:space-around;text-align:center">
    <div><div class="avatar" style="width:10px;height:10px;margin:0 auto" role="img" aria-label="Team member portrait"></div><div class="h" style="font-size:1.9px">Joel Tshala</div><div class="tx">Manager Marketing</div></div>
    <div><div class="avatar" style="width:10px;height:10px;margin:0 auto" role="img" aria-label="Team member portrait"></div><div class="h" style="font-size:1.9px">Marc Lunda</div><div class="tx">Manager Service</div></div>
  </div>
  <div class="abs" style="left:14px;top:51px;width:148px;display:flex;justify-content:space-around;text-align:center">
    <div><div class="avatar" style="width:10px;height:10px;margin:0 auto" role="img" aria-label="Team member portrait"></div><div class="h" style="font-size:1.9px">Sara Mwamba</div><div class="tx">Staff Marketing</div></div>
    <div><div class="avatar" style="width:10px;height:10px;margin:0 auto" role="img" aria-label="Team member portrait"></div><div class="h" style="font-size:1.9px">Leo Kalala</div><div class="tx">Staff Marketing</div></div>
    <div><div class="avatar" style="width:10px;height:10px;margin:0 auto" role="img" aria-label="Team member portrait"></div><div class="h" style="font-size:1.9px">Ines Mutombo</div><div class="tx">Staff Marketing</div></div>
    <div><div class="avatar" style="width:10px;height:10px;margin:0 auto" role="img" aria-label="Team member portrait"></div><div class="h" style="font-size:1.9px">Ruth Ngoy</div><div class="tx">Staff Service</div></div>
  </div>
  <div class="foot">varomel-mining.cd<span class="pg">page | 17</span></div><div class="badge"></div>
</section>

<section class="slide c6 r3">
  <div class="abs" style="left:8px;top:7px;font-size:5.8px;font-weight:700">Presentation <span style="color:var(--gold)">List</span></div>
  <svg class="abs" style="left:6px;top:18px" width="160" height="62" viewBox="0 0 160 62" font-family="Open Sans, sans-serif" font-size="1.8" fill="#555" text-anchor="middle">
    <line x1="4" y1="32" x2="156" y2="32" stroke="#ccc" stroke-width=".4" stroke-dasharray="1 1"/>
    <g fill="#e0a100"><circle cx="20" cy="32" r="3.6"/><circle cx="44" cy="32" r="3.6"/><circle cx="68" cy="32" r="3.6"/><circle cx="92" cy="32" r="3.6"/><circle cx="140" cy="32" r="3.6"/></g>
    <circle cx="116" cy="32" r="4.4" fill="#1b2a8c"/>
    <g fill="#fff" font-size="1.5"><text x="20" y="32.6">2021</text><text x="44" y="32.6">2022</text><text x="68" y="32.6">2023</text><text x="92" y="32.6">2024</text><text x="116" y="32.6">2025</text><text x="140" y="32.6">2026</text></g>
    <text x="44" y="8" font-weight="700" fill="#333">Lorem Ipsum</text><text x="44" y="11">First site won</text>
    <text x="92" y="8" font-weight="700" fill="#333">Lorem Ipsum</text><text x="92" y="11">Fleet doubled</text>
    <text x="140" y="8" font-weight="700" fill="#333">Lorem Ipsum</text><text x="140" y="11">Drone unit</text>
    <text x="20" y="51" font-weight="700" fill="#333">Lorem Ipsum</text><text x="20" y="54">Founded</text>
    <text x="68" y="51" font-weight="700" fill="#333">Lorem Ipsum</text><text x="68" y="54">New workshop</text>
    <text x="116" y="51" font-weight="700" fill="#333">The Goal</text><text x="116" y="54">Lead contractor</text>
  </svg>
  <div class="foot">varomel-mining.cd<span class="pg">page | 18</span></div><div class="badge"></div>
</section>

<!-- ROW 4 -->
<section class="slide c1 r4">
  <div class="abs" style="left:11px;top:27px;font-size:5.6px;font-weight:700;line-height:6.8px">Circle Graph<br><span style="color:var(--gold)">Analyse</span></div>
  <div class="abs tx" style="left:11px;top:54px;width:52px">Yearly review of project value shows steady growth month by month.</div>
  <svg class="abs" style="left:68px;top:24px" width="42" height="50" viewBox="0 0 42 50">
    <circle cx="20" cy="18" r="15" fill="none" stroke="#f2c94c" stroke-width="4"/>
    <circle cx="20" cy="18" r="15" fill="none" stroke="#e0a100" stroke-width="4" stroke-dasharray="40 95" transform="rotate(-90 20 18)"/>
    <circle cx="20" cy="18" r="15" fill="none" stroke="#c98a00" stroke-width="4" stroke-dasharray="18 95" stroke-dashoffset="-40" transform="rotate(-90 20 18)"/>
    <g font-family="Open Sans, sans-serif" font-size="1.6" fill="#555"><text x="1" y="44">■Jan ■Feb ■Mar ■Apr ■May ■Jun</text></g>
  </svg>
  <div class="abs" style="left:124px;top:23px;width:37px;height:18px;border:.4px solid #ccc">
    <div class="tx" style="margin:2px">June</div><div style="font-size:5px;text-align:right;margin-right:2px;color:#555">$5700</div></div>
  <div class="abs" style="left:124px;top:46px;width:37px;height:18px;border:.4px solid #ccc">
    <div class="tx" style="margin:2px">March</div><div style="font-size:5px;text-align:right;margin-right:2px;color:#555">$7600</div></div>
  <div class="foot">varomel-mining.cd<span class="pg">page | 19</span></div><div class="badge"></div>
</section>

<section class="slide c2 r4">
  <div class="title" style="top:10px">Infograph</div>
  <svg class="abs" style="left:10px;top:32px" width="152" height="45" viewBox="0 0 152 45" font-family="Open Sans, sans-serif" text-anchor="middle">
    <g fill="#fff" stroke="#f0d590" stroke-width=".5">
      <polygon points="13,2 22,7 22,17 13,22 4,17 4,7"/><polygon points="44,2 53,7 53,17 44,22 35,17 35,7"/><polygon points="75,2 84,7 84,17 75,22 66,17 66,7"/><polygon points="106,2 115,7 115,17 106,22 97,17 97,7"/><polygon points="137,2 146,7 146,17 137,22 128,17 128,7"/>
    </g>
    <g stroke="#ccc" stroke-width=".3"><line x1="23" y1="12" x2="34" y2="12"/><line x1="54" y1="12" x2="65" y2="12"/><line x1="85" y1="12" x2="96" y2="12"/><line x1="116" y1="12" x2="127" y2="12"/></g>
    <g font-size="2.1" fill="#444"><text x="13" y="13">Step 1</text><text x="44" y="13">Step 2</text><text x="75" y="13">Step 3</text><text x="106" y="13">Step 4</text><text x="137" y="13">Step 5</text></g>
    <g font-size="1.8" font-weight="700" fill="#333"><text x="13" y="30">Marketing Step</text><text x="44" y="30">Production Step</text><text x="75" y="30">R&amp;D Step</text><text x="106" y="30">Vendor Step</text><text x="137" y="30">Supplier Step</text></g>
    <g font-size="1.7" fill="#777"><text x="13" y="33.5">Find and reach</text><text x="13" y="36">mining clients</text><text x="44" y="33.5">Run the work</text><text x="44" y="36">on site daily</text><text x="75" y="33.5">Test new tools</text><text x="75" y="36">and methods</text><text x="106" y="33.5">Pick trusted</text><text x="106" y="36">vendors only</text><text x="137" y="33.5">Secure spares</text><text x="137" y="36">and fuel</text></g>
  </svg>
  <div class="foot">varomel-mining.cd<span class="pg">page | 20</span></div><div class="badge"></div>
</section>

<section class="slide c3 r4">
  <div class="title" style="top:10px">Infograph</div>
  <svg class="abs" style="left:10px;top:25px" width="152" height="55" viewBox="0 0 152 55" font-family="Open Sans, sans-serif" text-anchor="middle">
    <defs><linearGradient id="pill" x1="0" y1="0" x2="0" y2="1"><stop offset=".55" stop-color="#e0a100"/><stop offset=".55" stop-color="#1b2a8c"/></linearGradient></defs>
    <g fill="url(#pill)"><rect x="17" y="1" width="12" height="23" rx="6"/><rect x="55" y="1" width="12" height="23" rx="6"/><rect x="93" y="1" width="12" height="23" rx="6"/><rect x="131" y="1" width="12" height="23" rx="6"/></g>
    <g font-size="1.8" fill="#fff"><text x="23" y="11">One</text><text x="61" y="11">Two</text><text x="99" y="11">Three</text><text x="137" y="11">Four</text></g>
    <g font-size="1.7" fill="#777"><text x="23" y="29">Survey the site</text><text x="23" y="31.8">with drones</text><text x="61" y="29">Plan the pit</text><text x="61" y="31.8">and haul roads</text><text x="99" y="29">Mobilise fleet</text><text x="99" y="31.8">and crews</text><text x="137" y="29">Deliver and</text><text x="137" y="31.8">report daily</text></g>
    <g fill="#e0a100"><circle cx="23" cy="43" r="3.5"/><circle cx="61" cy="43" r="3.5"/><circle cx="99" cy="43" r="3.5"/><circle cx="137" cy="43" r="3.5"/></g>
    <g fill="none" stroke="#fff" stroke-width="2.4" stroke-linecap="round" stroke-linejoin="round">
      <use href="#i-search" x="21" y="41" width="4" height="4"/><use href="#i-chart" x="59" y="41" width="4" height="4"/><use href="#i-team" x="97" y="41" width="4" height="4"/><use href="#i-tick" x="135" y="41" width="4" height="4"/>
    </g>
  </svg>
  <div class="foot">varomel-mining.cd<span class="pg">page | 21</span></div><div class="badge"></div>
</section>

<section class="slide navy c4 r4">
  <div class="title" style="top:10px">Infograph</div>
  <div class="abs" style="left:13px;top:28px;width:146px;display:flex;gap:3px">
    <div style="flex:1;height:53px;border:.5px solid var(--gold);border-radius:2px;position:relative;padding:22px 3px 0"><div class="abs" style="left:9px;top:3px;width:15px;height:15px;border-radius:50%;background:var(--gold);font-size:3.6px;font-weight:700;text-align:center;line-height:14px">450</div><div class="h" style="color:#fff;font-size:2.2px">Step One</div><div class="tx w">Site survey and quote sent to the client.</div></div>
    <div style="flex:1;height:53px;border:.5px solid var(--gold);border-radius:2px;position:relative;padding:22px 3px 0"><div class="abs" style="left:9px;top:3px;width:15px;height:15px;border-radius:50%;background:var(--gold);font-size:3.6px;font-weight:700;text-align:center;line-height:14px">460</div><div class="h" style="color:#fff;font-size:2.2px">Step Two</div><div class="tx w">Contract signed and fleet booked in.</div></div>
    <div style="flex:1;height:53px;border:.5px solid var(--gold);border-radius:2px;position:relative;padding:22px 3px 0"><div class="abs" style="left:9px;top:3px;width:15px;height:15px;border-radius:50%;background:var(--gold);font-size:3.6px;font-weight:700;text-align:center;line-height:14px">480</div><div class="h" style="color:#fff;font-size:2.2px">Step Three</div><div class="tx w">Crews arrive and work starts on site.</div></div>
    <div style="flex:1;height:53px;border:.5px solid var(--gold);border-radius:2px;position:relative;padding:22px 3px 0"><div class="abs" style="left:9px;top:3px;width:15px;height:15px;border-radius:50%;background:var(--gold);font-size:3.6px;font-weight:700;text-align:center;line-height:14px">490</div><div class="h" style="color:#fff;font-size:2.2px">Step Four</div><div class="tx w">Weekly reports and final handover.</div></div>
  </div>
  <div class="foot">varomel-mining.cd<span class="pg">page | 22</span></div><div class="badge"></div>
</section>

<section class="slide c5 r4">
  <div class="title" style="top:10px">Date List <b>Agenda</b></div>
  <div class="abs" style="left:18px;top:27px;width:138px;display:flex;gap:6px">
    <div style="flex:1;height:50px;box-shadow:0 0 3px rgba(0,0,0,.12);text-align:center;padding-top:3px"><svg width="5" height="5" fill="none" stroke="#e0a100" stroke-width="2.4" stroke-linecap="round" stroke-linejoin="round"><use href="#i-flag" width="5" height="5"/></svg><div style="font-size:3px;font-weight:700;margin-top:1px">23<sup style="font-size:1.5px">rd</sup></div><div class="tx">June</div><div class="tx" style="text-align:left;padding:1px 3px">• Site kickoff<br>• Safety induction<br>• Fleet delivery<br>• Crew briefing</div></div>
    <div style="flex:1;height:50px;box-shadow:0 0 3px rgba(0,0,0,.12);text-align:center;padding-top:3px"><svg width="5" height="5" fill="none" stroke="#e0a100" stroke-width="2.4" stroke-linecap="round" stroke-linejoin="round"><use href="#i-chart" width="5" height="5"/></svg><div style="font-size:3px;font-weight:700;margin-top:1px">11<sup style="font-size:1.5px">st</sup></div><div class="tx">July</div><div class="tx" style="text-align:left;padding:1px 3px">• Drone survey<br>• Pit design review<br>• Road works begin<br>• Client report</div></div>
    <div style="flex:1;height:50px;box-shadow:0 0 3px rgba(0,0,0,.12);text-align:center;padding-top:3px"><svg width="5" height="5" fill="none" stroke="#e0a100" stroke-width="2.4" stroke-linecap="round" stroke-linejoin="round"><use href="#i-case" width="5" height="5"/></svg><div style="font-size:3px;font-weight:700;margin-top:1px">2<sup style="font-size:1.5px">nd</sup></div><div class="tx">August</div><div class="tx" style="text-align:left;padding:1px 3px">• Full haulage rate<br>• Mid-term audit<br>• Spares order<br>• Cost review</div></div>
  </div>
  <div class="foot">varomel-mining.cd<span class="pg">page | 23</span></div><div class="badge"></div>
</section>

<section class="slide c6 r4">
  <div class="title" style="top:10px">Monthly <b>Chart</b></div>
  <svg class="abs" style="left:10px;top:24px" width="152" height="52" viewBox="0 0 152 52" font-family="Open Sans, sans-serif" font-size="2" text-anchor="middle">
    <polyline points="12,22 30,12 47,28 66,20 86,28 104,22" fill="none" stroke="#f0c040" stroke-width=".5"/>
    <g fill="#333"><text x="10" y="20.5">60</text><text x="30" y="10">78</text><text x="47" y="31.5">49</text><text x="66" y="18.5">60</text><text x="86" y="31.5">49</text><text x="106" y="20.5">56</text></g>
    <g fill="#999" font-size="1.5"><text x="12" y="44">JAN</text><text x="30" y="44">FEB</text><text x="47" y="44">MAR</text><text x="66" y="44">APR</text><text x="86" y="44">MAY</text><text x="104" y="44">JUN</text></g>
    <circle cx="122" cy="4" r="3" fill="#e0a100"/><text x="122" y="4.7" fill="#fff" font-size="1.8">49</text>
    <text x="119" y="12" fill="#333" font-size="2.8" text-anchor="start">May</text>
    <text x="119" y="15.5" fill="#888" font-size="1.5" text-anchor="start">Output dipped in</text>
    <text x="119" y="17.7" fill="#888" font-size="1.5" text-anchor="start">the rainy weeks.</text>
    <circle cx="122" cy="30" r="3" fill="#e0a100"/><text x="122" y="30.7" fill="#fff" font-size="1.8">56</text>
    <text x="119" y="38" fill="#333" font-size="2.8" text-anchor="start">Jun</text>
    <text x="119" y="41.5" fill="#888" font-size="1.5" text-anchor="start">New trucks lifted</text>
    <text x="119" y="43.7" fill="#888" font-size="1.5" text-anchor="start">the monthly rate.</text>
  </svg>
  <div class="foot">varomel-mining.cd<span class="pg">page | 24</span></div><div class="badge"></div>
</section>

<!-- ROW 5 -->
<section class="slide c1 r5">
  <div class="title" style="top:12px">Three Point <b>Value</b></div>
  <svg class="abs" style="left:20px;top:30px" width="60" height="50" viewBox="0 0 60 50" font-family="Open Sans, sans-serif" font-size="2.8" text-anchor="middle">
    <polyline points="10,21 29,37 52,10" fill="none" stroke="#666" stroke-width="1.3"/>
    <g fill="#e0a100" stroke="#f4d77a" stroke-width=".8"><circle cx="10" cy="21" r="6"/><circle cx="29" cy="37" r="6"/><circle cx="52" cy="10" r="6"/></g>
    <g fill="#fff"><text x="10" y="22">One</text><text x="29" y="38">Two</text><text x="52" y="11">Three</text></g>
  </svg>
  <div class="abs" style="left:98px;top:30px;width:65px">
    <div style="font-size:3.4px">56%</div><div class="tx">Client projects finished ahead of plan.</div>
    <div style="font-size:3.4px;margin-top:3px">76%</div><div class="tx">Fleet hours in active production.</div>
    <div style="font-size:3.4px;margin-top:3px">89%</div><div class="tx">Staff hired from nearby communities.</div>
  </div>
  <div class="foot">varomel-mining.cd<span class="pg">page | 25</span></div><div class="badge"></div>
</section>

<section class="slide navy c2 r5">
  <div class="title" style="top:10px">Table Chart</div>
  <svg class="abs" style="left:24px;top:26px" width="122" height="56" viewBox="0 0 122 56" font-family="Open Sans, sans-serif" font-size="1.8" fill="#fff">
    <rect x="0" y="0" width="122" height="5" fill="#e0a100"/>
    <g font-weight="700"><text x="4" y="3.4">Data Name</text><text x="35" y="3.4">Number</text><text x="55" y="3.4">Profit Rate</text><text x="76" y="3.4">Option</text><text x="91" y="3.4">Rate</text><text x="102" y="3.4">Performance</text></g>
    <g fill="#2536a0"><rect y="13" width="122" height="7"/><rect y="27" width="122" height="7"/><rect y="41" width="122" height="7"/></g>
    <g stroke="#e0a100" stroke-width=".3"><line x1="0" y1="13" x2="122" y2="13"/><line x1="0" y1="27" x2="122" y2="27"/><line x1="0" y1="41" x2="122" y2="41"/></g>
    <g><text x="4" y="10">Data One</text><text x="37" y="10">5,667</text><text x="60" y="10">20.45</text><text x="78" y="10">Yes</text><text x="93" y="10">75</text><text x="107" y="10">3,566</text>
    <text x="4" y="17">Data Two</text><text x="37" y="17">6,5444</text><text x="60" y="17">34.5</text><text x="78" y="17">Yes</text><text x="93" y="17">67</text><text x="107" y="17">3,997</text>
    <text x="4" y="24">Data Three</text><text x="37" y="24">54,333</text><text x="60" y="24">56.7</text><text x="78" y="24">No</text><text x="93" y="24">77</text><text x="107" y="24">9,887</text>
    <text x="4" y="31">Data Four</text><text x="37" y="31">7,655</text><text x="60" y="31">6.55</text><text x="78" y="31">No</text><text x="93" y="31">89</text><text x="107" y="31">97,666</text>
    <text x="4" y="38">Data Five</text><text x="37" y="38">7,665</text><text x="60" y="38">90</text><text x="78" y="38">Yes</text><text x="93" y="38">90</text><text x="107" y="38">98.9</text>
    <text x="4" y="45">Data Six</text><text x="37" y="45">9,999</text><text x="60" y="45">69</text><text x="78" y="45">No</text><text x="93" y="45">87</text><text x="107" y="45">98.7</text></g>
  </svg>
  <div class="foot">varomel-mining.cd<span class="pg">page | 26</span></div><div class="badge"></div>
</section>

<section class="slide c3 r5">
  <div class="title" style="top:10px">Dashboard</div>
  <div class="abs" style="left:10px;top:23px;width:152px;display:flex;justify-content:space-around;text-align:center;color:#999">
    <div><div class="h" style="font-size:2px;color:#666">Project Done</div><div style="font-size:2.6px">563</div></div>
    <div><div class="h" style="font-size:2px;color:#666">Monthly Earning</div><div style="font-size:2.6px">$32,470</div></div>
    <div><div class="h" style="font-size:2px;color:#666">Costumer Acc</div><div style="font-size:2.6px">3,877</div></div>
    <div><div class="h" style="font-size:2px;color:#666">Claim</div><div style="font-size:2.6px">0</div></div>
  </div>
  <svg class="abs" style="left:10px;top:38px" width="152" height="44" viewBox="0 0 152 44" font-family="Open Sans, sans-serif" font-size="1.7" fill="#444">
    <text x="2" y="2" font-weight="700">5 Active Dashboard</text>
    <text x="2" y="13">Data Five</text><rect x="17" y="11.5" width="7" height="1.8" fill="#e0a100"/>
    <text x="2" y="18">Data Four</text><rect x="17" y="16.5" width="12" height="1.8" fill="#1b2a8c"/>
    <text x="2" y="23">Data Three</text><rect x="17" y="21.5" width="18" height="1.8" fill="#2536a0"/>
    <text x="2" y="28">Data Two</text><rect x="17" y="26.5" width="14" height="1.8" fill="#e0a100"/>
    <text x="2" y="33">Data One</text><rect x="17" y="31.5" width="20" height="1.8" fill="#f0c040"/>
    <text x="58" y="2" font-weight="700">2 User Per Role</text>
    <circle cx="70" cy="20" r="8" fill="none" stroke="#1b2a8c" stroke-width="3"/>
    <circle cx="70" cy="20" r="8" fill="none" stroke="#e0a100" stroke-width="3" stroke-dasharray="20 50"/>
    <text x="106" y="2" font-weight="700"># Live Profit and Net</text>
    <text x="116" y="9" font-size="2" fill="#666">Net Profit &amp; Net sales</text>
    <text x="124" y="17" font-size="2" fill="#666">Net profit</text>
    <text x="118" y="23" font-size="3.2" fill="#e0a100">$44.587M</text>
    <text x="118" y="29" font-size="2" fill="#666">Net sales = $15M</text>
  </svg>
  <div class="foot">varomel-mining.cd<span class="pg">page | 27</span></div><div class="badge"></div>
</section>

<section class="slide c4 r5">
  <div class="title" style="top:10px">Dashboard</div>
  <svg class="abs" style="left:8px;top:21px" width="158" height="60" viewBox="0 0 158 60" font-family="Open Sans, sans-serif" font-size="1.7" fill="#444">
    <text x="2" y="3">Data Statistics</text>
    <g fill="#e0a100"><rect x="14" y="12" width="2" height="14"/><rect x="22" y="8" width="2" height="18"/><rect x="30" y="14" width="2" height="12"/><rect x="38" y="6" width="2" height="20"/><rect x="46" y="11" width="2" height="15"/><rect x="54" y="9" width="2" height="17"/><rect x="62" y="5" width="2" height="21"/><rect x="70" y="12" width="2" height="14"/><rect x="78" y="7" width="2" height="19"/><rect x="86" y="10" width="2" height="16"/><rect x="94" y="8" width="2" height="18"/><rect x="102" y="4" width="2" height="22"/></g>
    <text x="122" y="3">Costumer Email</text>
    <circle cx="137" cy="16" r="8" fill="none" stroke="#1b2a8c" stroke-width=".6"/>
    <circle cx="137" cy="16" r="6" fill="none" stroke="#e0a100" stroke-width=".6" stroke-dasharray="25 40"/>
    <g font-size="1.8" text-anchor="middle">
      <text x="14" y="37" font-weight="700">Sales</text><text x="14" y="40">$7,620</text>
      <text x="53" y="37" font-weight="700">Revenue</text><text x="53" y="40">$4,280</text>
      <text x="92" y="37" font-weight="700">Clients</text><text x="92" y="40">$5,290</text>
      <text x="131" y="37" font-weight="700">Trade</text><text x="131" y="40">$7,780</text>
    </g>
    <path d="M2 54 L10 48 L16 51 L22 46 L28 50 V56 H2Z" fill="#f3d48a"/>
    <path d="M41 54 L49 47 L55 51 L61 45 L67 50 V56 H41Z" fill="#b9c2f0"/>
    <path d="M80 54 L88 48 L94 50 L100 46 L106 50 V56 H80Z" fill="#c7cbe6"/>
    <path d="M119 54 L127 47 L133 51 L139 45 L145 50 V56 H119Z" fill="#f6c5b0"/>
  </svg>
  <div class="foot">varomel-mining.cd<span class="pg">page | 28</span></div><div class="badge"></div>
</section>

<section class="slide c5 r5">
  <div class="title" style="top:10px">Dashboard</div>
  <svg class="abs" style="left:8px;top:22px" width="158" height="60" viewBox="0 0 158 60" font-family="Open Sans, sans-serif" font-size="1.6" fill="#444">
    <text x="4" y="2">Net Profit Margin</text>
    <polyline points="16,10 32,8 48,11 64,9 80,11 96,8 112,10" fill="none" stroke="#e0a100" stroke-width=".4"/>
    <polyline points="16,15 32,13 48,16 64,14 80,16 96,13 112,15" fill="none" stroke="#1b2a8c" stroke-width=".4"/>
    <text x="120" y="2">Rate Profitability Indicator</text>
    <rect x="140" y="5" width="8" height="1.5" fill="#1b2a8c"/><rect x="140" y="9" width="6" height="1.5" fill="#e0a100"/><rect x="140" y="13" width="7" height="1.5" fill="#c98a00"/><rect x="140" y="17" width="10" height="1.5" fill="#3a4aa0"/>
    <text x="4" y="24">Past Year vs Target vs Actual</text>
    <g fill="#1b2a8c"><rect x="10" y="46" width="1.3" height="8"/><rect x="22" y="44" width="1.3" height="10"/><rect x="34" y="42" width="1.3" height="12"/><rect x="46" y="44" width="1.3" height="10"/><rect x="58" y="40" width="1.3" height="14"/><rect x="70" y="42" width="1.3" height="12"/><rect x="82" y="38" width="1.3" height="16"/><rect x="94" y="40" width="1.3" height="14"/><rect x="106" y="36" width="1.3" height="18"/></g>
    <g fill="#e0a100"><rect x="12" y="44" width="1.3" height="10"/><rect x="24" y="43" width="1.3" height="11"/><rect x="36" y="40" width="1.3" height="14"/><rect x="48" y="42" width="1.3" height="12"/><rect x="60" y="38" width="1.3" height="16"/><rect x="72" y="40" width="1.3" height="14"/><rect x="84" y="36" width="1.3" height="18"/><rect x="96" y="38" width="1.3" height="16"/><rect x="108" y="34" width="1.3" height="20"/></g>
    <path d="M10 46 Q40 40 70 36 T110 34" fill="none" stroke="#c9a86a" stroke-width=".4"/>
    <circle cx="124" cy="38" r="1.2" fill="#e0a100"/><text x="127" y="38.6" font-size="2">68.780.930</text>
    <text x="122" y="43">Best result so far</text><text x="122" y="46">across active sites</text>
  </svg>
  <div class="foot">varomel-mining.cd<span class="pg">page | 29</span></div><div class="badge"></div>
</section>

<section class="slide c6 r5">
  <div class="title" style="top:10px">Dashboard</div>
  <svg class="abs" style="left:8px;top:22px" width="158" height="60" viewBox="0 0 158 60" font-family="Open Sans, sans-serif" font-size="1.5" fill="#888">
    <g text-anchor="middle"><text x="44" y="2">May</text><text x="58" y="2">Jun</text><text x="72" y="2">Jul</text><text x="86" y="2">Aug</text><text x="100" y="2">Sep</text><text x="114" y="2">Oct</text><text x="128" y="2">Nov</text><text x="142" y="2">Dec</text></g>
    <rect x="6" y="8" width="4" height="2" rx="1" fill="#e0a100"/><text x="12" y="9.6">Team One</text>
    <rect x="6" y="24" width="4" height="2" rx="1" fill="#8090e0"/><text x="12" y="25.6">Team Two</text>
    <rect x="6" y="40" width="4" height="2" rx="1" fill="#666"/><text x="12" y="41.6">Team Three</text>
    <rect x="42" y="9" width="18" height="3" rx="1.5" fill="#f0b400"/><rect x="90" y="9" width="58" height="3" rx="1.5" fill="#707070"/>
    <rect x="78" y="22" width="42" height="3" rx="1.5" fill="#8c98ee"/><rect x="62" y="27" width="24" height="3" rx="1.5" fill="#707070"/><rect x="96" y="27" width="44" height="3" rx="1.5" fill="#f0b400"/>
    <rect x="46" y="40" width="56" height="3" rx="1.5" fill="#f0b400"/><rect x="126" y="40" width="20" height="3" rx="1.5" fill="#8c98ee"/>
    <g text-anchor="middle"><text x="44" y="56">2023</text><text x="58" y="56">2023</text><text x="72" y="56">2023</text><text x="86" y="56">2023</text><text x="100" y="56">2023</text><text x="114" y="56">2023</text><text x="128" y="56">2023</text><text x="142" y="56">2023</text></g>
  </svg>
  <div class="foot">varomel-mining.cd<span class="pg">page | 30</span></div><div class="badge"></div>
</section>

<!-- ROW 6 -->
<section class="slide navy c1 r6">
  <div class="abs" style="top:27px;width:100%;text-align:center">
    <div style="font-size:9px;font-weight:700">Thank You</div>
    <div class="tx w" style="width:84px;margin:3px auto 0">Thank you for your time. We look forward to working with you on your next mining project.</div>
    <div style="display:flex;justify-content:center;gap:10px;margin-top:5px">
      <span style="width:4.5px;height:4.5px;border:.5px solid var(--gold);border-radius:50%"></span>
      <span style="width:4.5px;height:4.5px;border:.5px solid var(--gold);border-radius:50%"></span>
      <span style="width:4.5px;height:4.5px;border:.5px solid var(--gold);border-radius:50%"></span>
    </div>
  </div>
  <div class="foot">varomel-mining.cd<span class="pg">page |</span></div><div class="badge"></div>
</section>

<section class="slide c2 r6">
  <svg class="icon-sheet" style="left:12px;top:14px" width="148" height="68" viewBox="0 0 148 68" aria-label="Icon set" role="img">
    <g fill="none" stroke="#555" stroke-width="1.6" stroke-linecap="round" stroke-linejoin="round">
      <use href="#i-doc" x="2" y="2" width="7" height="7"/><use href="#i-team" x="29" y="2" width="7" height="7"/><use href="#i-case" x="56" y="2" width="7" height="7"/><use href="#i-gear" x="83" y="2" width="7" height="7"/><use href="#i-star" x="110" y="2" width="7" height="7"/><use href="#i-chart" x="137" y="2" width="7" height="7"/>
    </g>
    <g fill="none" stroke="#2a2a2a" stroke-width="2.6" stroke-linecap="round" stroke-linejoin="round">
      <use href="#i-clock" x="2" y="30" width="7" height="7"/><use href="#i-pin" x="29" y="30" width="7" height="7"/><use href="#i-monitor" x="56" y="30" width="7" height="7"/><use href="#i-pie" x="83" y="30" width="7" height="7"/><use href="#i-arrow" x="110" y="30" width="7" height="7"/><use href="#i-search" x="137" y="30" width="7" height="7"/>
      <use href="#i-user" x="2" y="56" width="7" height="7"/><use href="#i-rocket" x="29" y="56" width="7" height="7"/><use href="#i-tick" x="56" y="56" width="7" height="7"/><use href="#i-home" x="83" y="56" width="7" height="7"/><use href="#i-cloud" x="110" y="56" width="7" height="7"/><use href="#i-lock" x="137" y="56" width="7" height="7"/>
    </g>
  </svg>
</section>

<section class="slide c3 r6">
  <svg class="icon-sheet" width="157" height="81" viewBox="0 0 157 81" role="img" aria-label="Icon set"><rect x="0" y="0" width="157" height="81" fill="url(#icons-a)"/></svg>
</section>

<section class="slide c4 r6">
  <svg class="icon-sheet" width="157" height="81" viewBox="0 0 157 81" role="img" aria-label="Icon set"><rect x="0" y="0" width="157" height="81" fill="url(#icons-b)"/></svg>
</section>

<section class="slide c5 r6">
  <svg class="icon-sheet" width="157" height="81" viewBox="0 0 157 81" role="img" aria-label="Icon set"><g transform="translate(-29.4 0)"><rect x="29.4" y="0" width="157" height="81" fill="url(#icons-a)"/></g></svg>
</section>

<section class="slide c6 r6">
  <svg class="icon-sheet" width="157" height="81" viewBox="0 0 157 81" role="img" aria-label="Icon set"><g transform="translate(-39.2 0)"><rect x="39.2" y="0" width="157" height="81" fill="url(#icons-b)"/></g></svg>
</section>

</main>
</body>
</html>
```